Digital One Pager for Consulting Practice

I would like the essence of the content in my ppt consolidated into a one-pager. The one-pager will mainly be sent via email as a pdf and intended to excite and invite new clients and establish the credibility of my boutique high-end consulting firm. Infographics and symbols would be a plus. The target client should view the firm as providing premeir service. The client is getting a thought partner.

Target Market(s)

Large Medical Device Manufacturer Executives, Early-Stage Medical Device Manufacturer Executives, Partners at VC Firms

Industry/Entity Type

Medical Equipment

Colors
0355a3
f37122

Requirements
Must have
• Please match the color scheme in ppt. Please use the existing logo. I am very open to better graphics on the process. My photo does not need to be on the digital flyer. Hyper link to the website and email is needed.
Nice to have
• Infographics

```html
<!DOCTYPE html>
<html lang="en">
<head>
<meta charset="utf-8">
<title>Kestrel Advisory – One Pager</title>
<link href="https://fonts.googleapis.com/css2?family=Tinos:wght@400;700&family=Lato:wght@400;700;900&family=Montserrat:wght@700;800&display=swap" rel="stylesheet">
<style>
  :root{
    --navy:#13213f;
    --navy-deep:#0d1830;
    --ink:#0b0f1a;
    --orange:#f37122;
    --blue:#0355a3;
    --blue-1:#4f7fcf;
    --blue-2:#3f70c3;
    --blue-3:#2f61b6;
    --blue-4:#1f52aa;
    --white:#ffffff;
    --text:#1c1c24;
    --page:#e9e9ec;
  }
  *{box-sizing:border-box;margin:0;padding:0}
  html,body{width:1188px;height:1200px;overflow:hidden;background:var(--page)}
  body{position:relative;font-family:"Lato",Arial,sans-serif;color:var(--text)}

  .one-pager{position:absolute;left:154px;top:20px;width:880px;height:1160px;background:var(--white);overflow:hidden;box-shadow:0 2px 10px rgba(0,0,0,.12)}

  .hero-bg{position:absolute;left:0;top:0;width:880px;height:640px}

  .headline{position:absolute;left:0;top:80px;width:880px;text-align:center;font-family:"Tinos",serif;color:var(--white);font-size:44px;line-height:1.2;font-weight:400}

  .experience{position:absolute;left:58px;top:392px;width:490px;color:var(--white)}
  .section-title{font-family:"Tinos",serif;font-weight:700;font-size:29px;letter-spacing:.5px;margin-bottom:12px;white-space:nowrap}
  .experience ul{list-style:none}
  .experience li{position:relative;padding-left:22px;font-size:15px;line-height:1.3;margin-bottom:10px}
  .experience li::before{content:"";position:absolute;left:2px;top:6px;width:9px;height:9px;border-radius:50%;background:var(--white)}
  .experience .sub{margin-top:6px;margin-left:24px}
  .experience .sub li{margin-bottom:2px;font-size:14px}
  .experience .sub li::before{width:7px;height:7px;top:6px}

  .venn{position:absolute;left:565px;top:270px;width:300px;height:270px}

  .services{position:absolute;left:58px;top:680px;width:440px}
  .services .section-title{color:var(--ink);margin-bottom:8px}
  .service-cols{display:flex;gap:26px}
  .service-group{margin-bottom:14px}
  .service-group h3{font-family:"Tinos",serif;color:var(--orange);font-size:17px;font-weight:700;margin-bottom:4px;white-space:nowrap}
  .service-group ul{list-style:none;padding-left:12px}
  .service-group li{position:relative;padding-left:14px;font-size:14px;line-height:1.35;white-space:nowrap}
  .service-group li::before{content:"";position:absolute;left:0;top:7px;width:6px;height:6px;border-radius:50%;background:var(--ink)}

  .provide{position:absolute;left:510px;top:600px;width:340px;height:300px;background:var(--navy-deep);border-radius:28px;color:var(--white);padding:26px 26px}
  .provide h2{font-family:"Tinos",serif;font-weight:700;font-size:26px;margin-bottom:6px}
  .provide h3{font-size:15px;font-weight:900;margin:8px 0 6px}
  .provide ul{list-style:none}
  .provide li{position:relative;padding-left:16px;font-size:14px;line-height:1.35;margin-bottom:6px}
  .provide li::before{content:"";position:absolute;left:0;top:7px;width:7px;height:7px;border-radius:50%;background:var(--white)}

  .process{position:absolute;left:58px;top:930px;width:780px}
  .process .section-title{color:var(--ink);margin-bottom:12px}
  .process-steps{display:flex;align-items:stretch;height:66px}
  .step{position:relative;flex:1;display:flex;align-items:center;padding:0 20px 0 30px;color:var(--white);font-weight:700;font-size:16px;line-height:1.15;white-space:nowrap}
  .step:first-child{border-radius:18px 0 0 18px;padding-left:26px}
  .step:last-child{border-radius:0 18px 18px 0;flex:1.15}
  .step-1{background:var(--blue-1)}
  .step-2{background:var(--blue-2)}
  .step-3{background:var(--blue-3)}
  .step-4{background:var(--blue-4)}
  .step-arrow{position:absolute;right:-14px;top:50%;transform:translateY(-50%);width:28px;height:28px;z-index:2}

  .contact{position:absolute;right:42px;top:1048px;text-align:right}
  .phone{font-family:"Montserrat",sans-serif;font-weight:800;font-size:56px;color:var(--ink);letter-spacing:-1px;line-height:1}
  .links{margin-top:8px;font-size:15px;font-weight:700;color:var(--orange)}
  .links a{color:var(--orange);text-decoration:none}
  .links span{color:var(--ink);margin:0 4px}

  .brand{position:absolute;left:58px;top:1070px;display:flex;align-items:center;gap:12px}
  .brand-dot{width:26px;height:26px;border-radius:50%;background:var(--orange)}
  .brand-name{font-family:"Montserrat",sans-serif;font-weight:700;font-size:28px;letter-spacing:3px;color:var(--navy);line-height:1}
</style>
</head>
<body>
<main class="one-pager">

  <svg class="hero-bg" viewBox="0 0 880 640" aria-hidden="true">
    <rect width="880" height="640" fill="var(--orange)"/>
    <path d="M0 0H880V184C720 192 590 214 450 266C300 322 150 330 0 356Z" fill="var(--ink)"/>
    <path d="M0 0H880V172C720 180 590 202 450 254C300 310 150 318 0 344Z" fill="var(--orange)"/>
    <path d="M0 0H880V162C720 170 590 192 450 244C300 300 150 308 0 334Z" fill="var(--navy)"/>
  </svg>

  <h1 class="headline">Regulatory support for medtech firms.<br>Diligence for investors.</h1>

  <svg class="venn" viewBox="0 0 300 270" role="img" aria-label="Diagram: Experience, Network and Process overlapping around Leverage">
    <defs>
      <radialGradient id="sphere" cx="50%" cy="35%" r="65%">
        <stop offset="0" stop-color="#f2f2f4"/>
        <stop offset="1" stop-color="#6f7076"/>
      </radialGradient>
    </defs>
    <g stroke="#7fd6c8" stroke-width="1.5" fill="url(#sphere)">
      <circle cx="80" cy="95" r="72"/>
      <circle cx="220" cy="85" r="72"/>
      <circle cx="155" cy="190" r="72"/>
    </g>
    <circle cx="150" cy="118" r="38" fill="var(--navy)" stroke="#7fd6c8" stroke-width="1.5"/>
    <g font-family="Tinos, serif" font-size="13" fill="#fff" text-anchor="middle" text-decoration="underline">
      <text x="62" y="98">Experience</text>
      <text x="236" y="80">Network</text>
      <text x="150" y="122">Leverage</text>
      <text x="158" y="226">Process</text>
    </g>
  </svg>

  <section class="experience">
    <h2 class="section-title">EXPERIENCE:</h2>
    <ul>
      <li>Over a decade @FDA (Former Deputy Division Director)</li>
      <li>Expertise: Cardiovascular, Ophthalmology, General Hospital, Infection Control, Dental, Anesthesia, Respiratory</li>
      <li>Vice President Regulatory Affairs / Quality Assurance @Corvane (Fortune 150 Company)
        <ul class="sub">
          <li>Initiated reorganization of department</li>
          <li>Led major compliance effort</li>
          <li>Successful FDA inspection (no observations)</li>
        </ul>
      </li>
    </ul>
  </section>

  <section class="provide">
    <h2>Experience to Provide...</h2>
    <h3>Executive Application Review</h3>
    <ul>
      <li>Examples include: Presubmission, IDE, 510(k), 513(g), PMA, Refuse to Accept, Hold letter</li>
      <li>Troubleshooting</li>
    </ul>
    <h3>Strategic Advice &amp; Diligence to Investors</h3>
    <ul>
      <li>Validate &amp; Verify Founder Milestones</li>
      <li>Diligence portfolio company Regulatory and Quality systems</li>
    </ul>
  </section>

  <section class="services">
    <h2 class="section-title">SERVICES:</h2>
    <div class="service-cols">
      <div>
        <div class="service-group">
          <h3>Regulatory Strategy</h3>
          <ul><li>RAQA Organizational Structure</li><li>Regulatory Pathway</li></ul>
        </div>
        <div class="service-group">
          <h3>Interim Executive Leadership</h3>
          <ul><li>Compliance Remediation</li><li>Accelerated Product Registration</li></ul>
        </div>
      </div>
      <div>
        <div class="service-group">
          <h3>FDA Communications</h3>
          <ul><li>Deficiency Response</li><li>Application Review</li></ul>
        </div>
        <div class="service-group">
          <h3>Training</h3>
          <ul><li>FDA Communication</li><li>MDR Reporting</li></ul>
        </div>
      </div>
    </div>
  </section>

  <section class="process">
    <h2 class="section-title">EFFICIENT PROCESS:</h2>
    <div class="process-steps">
      <div class="step step-1">Exploratory<br>Call
        <svg class="step-arrow" viewBox="0 0 28 28" aria-hidden="true"><circle cx="14" cy="14" r="13" fill="#fff"/><path d="M8 14H19M15 9.5L19.5 14L15 18.5" stroke="var(--blue-2)" stroke-width="2.6" fill="none" stroke-linecap="round" stroke-linejoin="round"/></svg>
      </div>
      <div class="step step-2">Regulatory<br>Landscape
        <svg class="step-arrow" viewBox="0 0 28 28" aria-hidden="true"><circle cx="14" cy="14" r="13" fill="#fff"/><path d="M8 14H19M15 9.5L19.5 14L15 18.5" stroke="var(--blue-3)" stroke-width="2.6" fill="none" stroke-linecap="round" stroke-linejoin="round"/></svg>
      </div>
      <div class="step step-3">Problem<br>Statement
        <svg class="step-arrow" viewBox="0 0 28 28" aria-hidden="true"><circle cx="14" cy="14" r="13" fill="#fff"/><path d="M8 14H19M15 9.5L19.5 14L15 18.5" stroke="var(--blue-4)" stroke-width="2.6" fill="none" stroke-linecap="round" stroke-linejoin="round"/></svg>
      </div>
      <div class="step step-4">Review &amp; Align on<br>Deliverables</div>
    </div>
  </section>

  <div class="contact">
    <div class="phone">202.555.0148</div>
    <div class="links"><a href="mailto:info@kestreladvisory.com">info@kestreladvisory.com</a><span>|</span><a href="https://www.kestreladvisory.com">www.kestreladvisory.com</a></div>
  </div>

  <div class="brand">
    <span class="brand-dot" aria-hidden="true"></span>
    <span class="brand-name">KESTREL ADVISORY</span>
  </div>

</main>
</body>
</html>
```